Business Card Design

Harbor Refuse 284 is a waste collection business contracted to remove waste from city streets, parks and caravan parks.

Target Market(s)

CEO and Managing Directors

Industry/Entity Type

Business

Contact Information for Business Card

Harbor Refuse 284
Manager
Glen Parkes
0438261954
harborrefuse284@mailbox-example.com.au

Colors
33a6d7
ecf7fb

Requirements
Must have
• Must have eye catching design that stands out above others ( tender process can be very competitive ).
Nice to have
• A garbage truck on or in the logo somehow

```html
<!DOCTYPE html>
<html lang="en">
<head>
<meta charset="utf-8">
<title>Harbor Refuse 284 — Business Card</title>
<link rel="stylesheet" href="https://fonts.googleapis.com/css2?family=Open+Sans:wght@400;600;700&display=swap">
<style>
  :root {
    --backdrop: #d9e6ec;
    --card: #ffffff;
    --card-foot: #ecf7fb;
    --brand-blue: #33a6d7;
    --band-blue: #33a6d7;
    --ink: #1f1f1f;
    --band-text: #ffffff;
  }
  * { box-sizing: border-box; margin: 0; padding: 0; }
  html, body {
    width: 1200px;
    height: 827px;
    overflow: hidden;
  }
  body {
    background: var(--backdrop);
    font-family: "Open Sans", Arial, sans-serif;
    display: flex;
    align-items: center;
    justify-content: center;
  }
  .business-card {
    position: relative;
    width: 1000px;
    height: 571px;
    background: var(--card);
    border-radius: 34px;
    overflow: hidden;
    box-shadow: 0 10px 30px rgba(0, 0, 0, 0.18);
  }
  .card-foot {
    position: absolute;
    left: 0;
    bottom: 0;
    width: 100%;
    height: 94px;
    background: var(--card-foot);
  }
  .brand {
    position: absolute;
    left: 150px;
    top: 120px;
    display: flex;
    align-items: center;
    gap: 40px;
  }
  .brand-name {
    font-size: 60px;
    font-weight: 700;
    color: var(--brand-blue);
    letter-spacing: -0.5px;
    line-height: 1;
  }
  .truck-illustration {
    width: 210px;
    height: 130px;
    display: block;
  }
  .contact-band {
    position: absolute;
    left: 0;
    top: 345px;
    width: 100%;
    height: 132px;
    background: var(--band-blue);
    color: var(--band-text);
  }
  .person {
    position: absolute;
    left: 140px;
    top: 30px;
  }
  .person-name {
    font-size: 38px;
    font-weight: 400;
    letter-spacing: 0.5px;
    line-height: 1.1;
  }
  .person-title {
    font-size: 22px;
    font-weight: 400;
    letter-spacing: 1px;
    margin-top: 4px;
    margin-left: 16px;
  }
  .contact-lines {
    position: absolute;
    left: 530px;
    top: 24px;
  }
  .phone {
    font-size: 34px;
    font-weight: 400;
    letter-spacing: 0.5px;
    line-height: 1.2;
  }
  .phone-number {
    font-weight: 700;
    margin-left: 10px;
  }
  .email {
    font-size: 19px;
    font-weight: 400;
    margin-top: 8px;
    white-space: nowrap;
  }
</style>
</head>
<body>
  <main class="business-card">
    <header class="brand">
      <span class="brand-name">Harbor Refuse 284</span>
      <svg class="truck-illustration" role="img" aria-label="Illustration of a garbage collection truck" viewBox="0 0 210 130">
        <defs>
          <linearGradient id="truckTone" x1="0" y1="0" x2="1" y2="1">
            <stop offset="0" stop-color="#ecf7fb"/>
            <stop offset="1" stop-color="#8a9aa2"/>
          </linearGradient>
        </defs>
        <rect x="0" y="0" width="210" height="130" rx="6" fill="url(#truckTone)"/>
      </svg>
    </header>

    <section class="contact-band">
      <div class="person">
        <p class="person-name">GLEN PARKES</p>
        <p class="person-title">MANAGER</p>
      </div>
      <div class="contact-lines">
        <p class="phone">CALL:<span class="phone-number">0438261954</span></p>
        <p class="email">harborrefuse284@mailbox-example.com.au</p>
      </div>
    </section>

    <div class="card-foot"></div>
  </main>
</body>
</html>
```